Lakeshore Freightways Guild Web Update

Update wordpress based association web site. Please look up www.lakeshorefreightwaysguild.com for our web site to get a feel for what we currently having. We would like our updated web site to look similar to: www.brightoakline.com. We will provide our key points for updating in a future email.

Target Market(s)

duplicate the brightoakline.com format please.

Number of Pages Required

4 page

Font styles to use
Serif

Requirements
Must have
• duplicate the brightoakline.com format please. You will keep most of the content that we currently have on our website.
Nice to have
• n/a
Should not have
• n/a

```html
<!DOCTYPE html>
<html lang="en">
<head>
<meta charset="utf-8">
<title>Lakeshore Freightways Guild</title>
<link rel="stylesheet" href="https://fonts.googleapis.com/css2?family=Hind:wght@400;500;600;700&display=swap">
<style>
:root{
  --navy:#0d1a6b;
  --green:#0a9444;
  --green-dark:#123d22;
  --panel-green:rgba(38,108,58,0.82);
  --text-dark:#2b3a30;
  --grey:#8a8a8a;
  --white:#ffffff;
  --rule:#d9d9d9;
}
*{box-sizing:border-box;margin:0;padding:0}
html,body{width:1200px;height:1000px;overflow:hidden;background:var(--white);font-family:"Hind",sans-serif}
.page{position:relative;width:1200px;height:1000px;overflow:hidden}

.site-header{position:absolute;top:0;left:0;width:1200px;height:110px;background:var(--white);border-bottom:1px solid var(--rule)}
.brand{position:absolute;left:30px;top:8px;display:flex;align-items:center;gap:10px}
.brand-mark{width:22px;height:22px;background:var(--navy)}
.brand-name{font-size:20px;font-weight:600;color:var(--navy);line-height:1.1;width:120px}
.social{position:absolute;right:50px;top:0;display:flex}
.social-item{width:32px;height:33px;display:flex;align-items:center;justify-content:center;border-left:1px solid var(--rule)}
.social-item:first-child{border-left:none}
.social-dot{width:16px;height:16px;background:var(--green-dark);border-radius:50%}
.social-item.video .social-dot{background:#d24a32;border-radius:2px}
.menu-btn{position:absolute;left:980px;top:58px;width:80px;height:40px;border:2px solid var(--grey);border-radius:2px;color:var(--grey);font-size:17px;font-weight:500;display:flex;align-items:center;padding-left:6px;gap:5px}
.menu-btn svg{display:block}
.login-btn{position:absolute;left:1077px;top:57px;width:61px;height:41px;background:var(--green);border:1px solid #0b7a38;color:var(--white);font-size:18px;font-weight:500;display:flex;align-items:center;justify-content:center;padding-top:2px}

.hero{position:absolute;top:111px;left:0;width:1200px;height:538px;background:linear-gradient(180deg,#4e6a8c 0%,#8aa3bd 40%,#b6c3cf 70%,#dfe6ee 100%)}
.hero-text{position:absolute;left:125px;top:308px;width:960px;color:var(--white);font-size:20px;font-weight:600;line-height:29px;letter-spacing:0.3px;text-shadow:0 1px 2px rgba(0,0,0,0.4)}
.hero-arrow{position:absolute;left:578px;top:476px}

.nav-panel{position:absolute;left:674px;top:111px;width:475px;height:201px;background:var(--white);padding:30px 0 0 31px;display:flex}
.nav-col{list-style:none;width:195px}
.nav-col + .nav-col{margin-left:32px}
.nav-col li{height:34px;line-height:36px;padding-left:11px;font-size:15px;color:var(--text-dark);letter-spacing:0.5px}
.nav-col li.active{background:var(--green);color:var(--white);font-weight:600}

.section-title{position:absolute;top:708px;left:0;width:1200px;text-align:center;font-size:35px;font-weight:600;color:var(--green-dark);letter-spacing:1px}

.welcome{position:absolute;top:801px;left:0;width:1200px;height:199px;background:linear-gradient(90deg,#3f5a33 0%,#7e8c6a 30%,#6f7e60 50%,#55704a 75%,#47603e 100%)}
.welcome-card{position:absolute;left:566px;top:0;width:584px;height:199px;background:var(--panel-green);padding:20px 0 0 36px;color:var(--white)}
.welcome-name{font-size:36px;font-weight:600;line-height:37px;letter-spacing:1.5px}
.welcome-body{margin-top:10px;width:545px;font-size:16.5px;line-height:29px;letter-spacing:0.6px}
</style>
</head>
<body>
<div class="page">
  <header class="site-header">
    <div class="brand">
      <span class="brand-mark"></span>
      <span class="brand-name">Lakeshore Freightways Guild</span>
    </div>
    <div class="social">
      <span class="social-item"><span class="social-dot"></span></span>
      <span class="social-item"><span class="social-dot"></span></span>
      <span class="social-item"><span class="social-dot"></span></span>
      <span class="social-item"><span class="social-dot"></span></span>
      <span class="social-item video"><span class="social-dot"></span></span>
    </div>
    <div class="menu-btn">Menu
      <svg width="17" height="12" viewBox="0 0 17 12"><g fill="#8a8a8a"><rect y="0" width="17" height="2"/><rect y="5" width="17" height="2"/><rect y="10" width="17" height="2"/></g></svg>
    </div>
    <div class="login-btn">login</div>
  </header>

  <section class="hero" role="img" aria-label="Freight locomotive ploughing through snow past a railway crossing signal">
    <p class="hero-text">Railroad company investments – along with education, safety-enhancing technologies and training – have helped ensure that train accidents are at an all-time low.</p>
    <svg class="hero-arrow" width="84" height="50" viewBox="0 0 84 50"><polyline points="5,5 42,42 79,5" fill="none" stroke="#ffffff" stroke-width="9" stroke-linecap="round" stroke-linejoin="round"/></svg>
  </section>

  <nav class="nav-panel">
    <ul class="nav-col">
      <li class="active">Home</li>
      <li>What we do</li>
      <li>Who we are</li>
      <li>Who is serve</li>
    </ul>
    <ul class="nav-col">
      <li>Resouces</li>
    </ul>
  </nav>

  <h2 class="section-title">Get on the Brightoak Path</h2>

  <section class="welcome" role="img" aria-label="Freight train of tank cars passing through green trees">
    <div class="welcome-card">
      <h3 class="welcome-name">Dale Porter<br>President</h3>
      <p class="welcome-body">I would like to welcome you to the Lakeshore Freightways Guild website. Here you will find valuable information on Michigan railroads, including issues and concerns in and around the railroad industry. We are an active and aggressive state railroad association and</p>
    </div>
  </section>
</div>
</body>
</html>
```